Launching a new real estate agency in Monaco

Hello, I am opening a new real estate agency in Monaco. For the purpose of my activity, in order to be known quickly among a fierce competition I need an advertising campaign that will be broadcast in local magazines, newspapers, paper board, etc.

You will find example of pictures of Monaco on which I have the rights and my logo. You can always pick other images that I can buy if the price is reasonable for a commercial use (<200 $)

Please respect the color code.

I wish you good luck and look forward to give you my feedbacks

Reason: Only few projects posted were respecting the brief and of quality. Hoping to receive more in coming days

Target Market(s)

International high-end clientele of all ages, all genders.

Industry/Entity Type

Real Estate Agent

Font styles to use
Serif

Requirements
Must have
• 1/ My logo
• 2/ This message "Un nouveau regard sur l'immobilier" means in English a fresh look at real estate or new eyes on real-estate.
• 3/ My address: 14 rue des Orvilles, Passage Marcellin, 98 000 Monaco
• 4/ Phone number: +377.93.48.25.71
• 5/ Website: www.brunor-agency.com.
• 6/ Format: Files should be easily adjustable but I'd like a vertical display to fit easily in Magazines, Poster and billboard. So please work in high resolution !
Nice to have
• Please think about your design in accordance with the message I want to display.
Should not have
• A simple poster with a picture of Monaco that does not take into consideration the message of the advertisement, "Un nouveau regard sur l'immobilier" which means in english, new eyes on real-estate or a new look at real-estate, or new vision at real-estate.

```html
<!DOCTYPE html>
<html lang="fr">
<head>
<meta charset="utf-8">
<title>Brunor Agency – Un nouveau regard sur l’immobilier</title>
<link rel="stylesheet" href="https://fonts.googleapis.com/css2?family=Josefin+Slab:wght@400;600;700&display=swap">
<style>
  :root {
    --backdrop: #1c1c1c;
    --navy: #1f2a40;
    --pin-fill: #232a36;
    --pin-edge: #3a4252;
    --pin-glow: #4fb6ff;
    --headline: #f4eef0;
    --info-text: #c9ccd4;
    --copper: #d9a08a;
    --sky-top: #4e3a55;
    --sky-mid: #5b3f57;
    --bay: #3a2c42;
    --city-glow: #8a4a2c;
    --city-dark: #2a1d24;
  }
  * { margin: 0; padding: 0; box-sizing: border-box; }
  html, body {
    width: 800px;
    height: 1200px;
    overflow: hidden;
    background: var(--backdrop);
    font-family: "Josefin Slab", serif;
  }
  .advert {
    position: absolute;
    left: 30px;
    top: 116px;
    width: 740px;
    height: 967px;
    overflow: hidden;
  }
  .hero-photo {
    position: absolute;
    left: 0;
    top: 0;
    width: 740px;
    height: 761px;
    background:
      radial-gradient(ellipse 40% 30% at 60% 82%, rgba(230,140,50,0.6), transparent 70%),
      radial-gradient(ellipse 25% 20% at 16% 62%, rgba(235,180,100,0.5), transparent 70%),
      radial-gradient(ellipse 35% 12% at 70% 18%, rgba(200,120,80,0.35), transparent 70%),
      linear-gradient(180deg, var(--sky-top) 0%, var(--sky-mid) 18%, var(--bay) 42%, var(--city-glow) 72%, var(--city-dark) 100%);
  }
  .pin-layer {
    position: absolute;
    left: 0;
    top: 0;
    width: 740px;
    height: 761px;
  }
  .headline {
    position: absolute;
    left: 59px;
    top: 192px;
    color: var(--headline);
    font-size: 31px;
    font-weight: 400;
    letter-spacing: 3px;
    line-height: 39px;
    text-transform: uppercase;
  }
  .headline strong { font-weight: 700; }
  .info-band {
    position: absolute;
    left: 0;
    top: 761px;
    width: 740px;
    height: 206px;
    background: var(--navy);
  }
  .address {
    position: absolute;
    left: 59px;
    top: 54px;
    color: var(--info-text);
    font-size: 16px;
    letter-spacing: 1px;
    line-height: 22px;
  }
  .phone {
    position: absolute;
    left: 59px;
    top: 144px;
    color: #ffffff;
    font-size: 15px;
    font-weight: 700;
    letter-spacing: 1px;
  }
  .brand {
    position: absolute;
    left: 362px;
    top: 58px;
    display: flex;
    align-items: center;
    gap: 14px;
  }
  .brand-mark {
    width: 22px;
    height: 22px;
    background: var(--copper);
  }
  .brand-name {
    color: var(--copper);
    font-size: 32px;
    font-weight: 700;
    letter-spacing: 2px;
    white-space: nowrap;
  }
  .website {
    position: absolute;
    left: 464px;
    top: 140px;
    color: #ffffff;
    font-size: 16px;
    font-weight: 600;
    letter-spacing: 1.5px;
  }
</style>
</head>
<body>
  <main class="advert">
    <div class="hero-photo" role="img" aria-label="Aerial night view of Monaco's coastline, bay and illuminated towers under a violet dusk sky"></div>

    <svg class="pin-layer" viewBox="0 0 740 761" aria-hidden="true">
      <defs>
        <radialGradient id="pin-shade" cx="0.35" cy="0.3" r="0.8">
          <stop offset="0" stop-color="#3a4252"/>
          <stop offset="1" stop-color="#1a202b"/>
        </radialGradient>
        <radialGradient id="base-glow" cx="0.5" cy="0.5" r="0.5">
          <stop offset="0" stop-color="#bfe6ff" stop-opacity="0.95"/>
          <stop offset="1" stop-color="#4fb6ff" stop-opacity="0"/>
        </radialGradient>
        <symbol id="map-pin" viewBox="0 0 100 140">
          <ellipse cx="50" cy="130" rx="30" ry="9" fill="url(#base-glow)"/>
          <path d="M50 128 C38 104 8 82 8 46 A42 42 0 0 1 92 46 C92 82 62 104 50 128 Z" fill="url(#pin-shade)" stroke="#3a4252" stroke-width="1.5"/>
          <circle cx="50" cy="46" r="17" fill="none" stroke="#d9a08a" stroke-width="5"/>
        </symbol>
      </defs>
      <use class="map-pin" href="#map-pin" x="571" y="71" width="24" height="34"/>
      <use class="map-pin" href="#map-pin" x="602" y="77" width="24" height="34"/>
      <use class="map-pin" href="#map-pin" x="479" y="101" width="24" height="34"/>
      <use class="map-pin" href="#map-pin" x="529" y="123" width="27" height="38"/>
      <use class="map-pin" href="#map-pin" x="672" y="93" width="33" height="46"/>
      <use class="map-pin" href="#map-pin" x="717" y="189" width="46" height="64"/>
      <use class="map-pin" href="#map-pin" x="537" y="179" width="124" height="174"/>
      <use class="map-pin" href="#map-pin" x="340" y="235" width="72" height="101"/>
      <use class="map-pin" href="#map-pin" x="261" y="333" width="72" height="101"/>
      <use class="map-pin" href="#map-pin" x="535" y="385" width="85" height="119"/>
      <use class="map-pin" href="#map-pin" x="353" y="401" width="105" height="147"/>
    </svg>

    <h1 class="headline">Un <strong>nouveau</strong><br><strong>regard</strong> sur<br>l’immobilier.</h1>

    <footer class="info-band">
      <p class="address">14 rue des Orvilles,<br>Passage Marcellin<br>98 000 Monaco</p>
      <p class="phone">+377.93.48.25.71</p>
      <div class="brand">
        <span class="brand-mark"></span>
        <span class="brand-name">BRUNOR AGENCY</span>
      </div>
      <p class="website">www.brunor-agency.com</p>
    </footer>
  </main>
</body>
</html>
```